To design the Curriculum Vitae of a General Manager Legal

the objective is to redesign the attached Résumé for a senior level Internal Legal Executive in order to make it attractive, easily readable, catchy, modern looking while staying classy, elegant, sobre, and serious.
The résumé is attached to this project. it contains the followings sections : Photo; Contact Details; Summary; Education; Experience; Other.
Feel free to use photoshop to improve photo.
Updates

Target Market(s)

Legal community; law firms; Big corporations requiring internal legal senior executive

Font styles to use
Serif

Colors
ffffff
85cae6
33a6d7
0292cd
86cfc6
cfeae6
757575
919191
d9d9d9

Requirements
Must have
• classy; serious; professional; elegant; easy to read; catchy; modern;

```html
<!DOCTYPE html>
<html lang="en">
<head>
<meta charset="utf-8">
<title>Lina Haddad El Rami – Curriculum Vitae</title>
<link rel="stylesheet" href="https://fonts.googleapis.com/css2?family=Montserrat:wght@400;500;600;700&family=Raleway:wght@300;400&display=swap">
<style>
:root{
  --band:#9fc6d1;
  --band-line:#cfe3ea;
  --sidebar:#d3e5eb;
  --heading-bg:#dde9ed;
  --ink:#3d3d3d;
  --text:#5a5a5a;
  --muted:#757575;
  --rule:#d9d9d9;
  --backdrop:#ebebeb;
  --paper:#ffffff;
  --accent:#33a6d7;
}
*{box-sizing:border-box;margin:0;padding:0}
html,body{width:1200px;height:3000px;overflow:hidden}
body{background:var(--backdrop);font-family:"Montserrat",Arial,sans-serif;color:var(--text);position:relative}

/* ===== main page ===== */
.cv-page{position:absolute;left:70px;top:70px;width:1100px;height:1500px;background:var(--paper);box-shadow:0 2px 10px rgba(0,0,0,.08)}
.cv-header{position:absolute;left:0;top:0;width:1100px;height:180px;background:var(--band);border-top:6px solid var(--band-line)}
.cv-header::after{content:"";position:absolute;left:0;right:0;bottom:10px;height:2px;background:var(--band-line)}
.cv-name{position:absolute;left:0;right:0;top:22px;text-align:center;font-family:"Raleway",Arial,sans-serif;font-weight:300;font-size:54px;letter-spacing:.3em;line-height:66px;color:#fff}
.cv-name .surname{display:block;color:#4a4a4a;font-weight:400;letter-spacing:.12em}

.sidebar{position:absolute;left:20px;top:290px;width:294px;height:1130px;background:var(--sidebar);overflow:hidden}
.photo{position:absolute;left:17px;top:20px;width:260px;height:260px;border-radius:50%;border:5px solid var(--band);background:radial-gradient(circle at 50% 45%,#b99a86 0%,#7a5a4a 55%,#4a3a34 100%)}
.side-heading{position:absolute;left:20px;width:254px;height:46px;background:var(--band);color:#fff;font-weight:500;font-size:23px;text-align:center;line-height:46px;letter-spacing:.02em}
.contact-row{position:absolute;left:22px;display:flex;align-items:center;gap:12px;font-size:16px;font-weight:600;color:var(--ink)}
.contact-row svg{width:28px;height:28px}
.side-block{position:absolute;left:20px;width:258px;font-size:14px;line-height:18.5px;color:var(--ink);letter-spacing:-.1px}
.side-block h4{font-weight:700;font-size:14px;margin-bottom:3px}
.side-block ul{list-style:none;margin-bottom:14px}
.side-block li{position:relative;padding-left:18px;margin-bottom:2px}
.side-block li::before{content:"";position:absolute;left:4px;top:7px;width:5px;height:5px;border-radius:50%;background:var(--muted)}

.main-col{position:absolute;left:366px;top:296px;width:700px}
.section-bar{height:40px;background:var(--heading-bg);border-left:3px solid var(--band);font-weight:700;font-size:30px;line-height:40px;color:var(--ink);padding-left:8px;letter-spacing:.02em}
.summary p{font-size:17px;line-height:21.5px;color:var(--text);margin:16px 0 0 8px}
.summary p:first-of-type{margin-top:18px}
.experience{margin-top:28px}
.role{display:flex;margin:30px 0 0 8px;font-size:17px;line-height:21px}
.role .dates{width:236px;color:var(--ink)}
.role .title{flex:1;font-weight:700;color:var(--ink)}
.desc h3{font-size:21px;font-weight:600;color:var(--ink);margin:34px 0 0 8px}
.desc p{font-size:17px;line-height:21.5px;margin:2px 0 0 8px}
.cv-footer{position:absolute;left:0;bottom:0;width:1100px;height:30px;background:var(--band)}

/* ===== continuation pages ===== */
.sheet{position:absolute;background:var(--paper);box-shadow:0 2px 8px rgba(0,0,0,.1);padding:22px 24px;font-size:7.4px;line-height:9.4px;color:var(--ink);overflow:hidden}
.sheet::after{content:"";position:absolute;left:0;right:0;bottom:0;height:14px;background:var(--band)}
.sheet h5{font-size:7.6px;font-weight:700;margin:4px 0 2px}
.sheet h6{font-size:7.2px;font-weight:700;text-decoration:underline;margin:5px 0 1px}
.sheet p{margin-bottom:3px}
.sheet ul{list-style:none;margin-bottom:4px}
.sheet li{position:relative;padding-left:8px;margin-bottom:1px}
.sheet li::before{content:"";position:absolute;left:1px;top:3.5px;width:3px;height:3px;border-radius:50%;background:var(--ink)}
.entry{display:flex;margin-bottom:16px}
.entry .when{width:46%;padding-right:8px}
.entry .what{flex:1}
.two-col{display:flex;gap:18px;margin-bottom:20px}
.two-col > div{flex:1}
.sheet-2{left:130px;top:1610px;width:460px;height:620px}
.sheet-3{left:630px;top:1610px;width:470px;height:620px}
.sheet-4{left:130px;top:2250px;width:460px;height:660px}
.sheet-5{left:630px;top:2250px;width:470px;height:660px}
</style>
</head>
<body>

<section class="cv-page">
  <header class="cv-header">
    <h1 class="cv-name">LINA HADDAD <span class="surname">EL RAMI</span></h1>
  </header>

  <aside class="sidebar">
    <div class="photo" role="img" aria-label="Portrait photograph of the candidate"></div>

    <div class="side-heading" style="top:334px">CONTACT</div>
    <div class="contact-row" style="top:398px">
      <svg viewBox="0 0 30 30" aria-hidden="true"><rect x="1" y="1" width="28" height="28" fill="none" stroke="#757575" stroke-width="1.5"/><rect x="7" y="10" width="16" height="11" fill="none" stroke="#757575" stroke-width="1.5"/><path d="M7 10l8 6 8-6" fill="none" stroke="#757575" stroke-width="1.5"/></svg>
      lina.elrami@mailbox.com
    </div>
    <div class="contact-row" style="top:444px">
      <svg viewBox="0 0 30 30" aria-hidden="true"><rect x="1" y="1" width="28" height="28" fill="none" stroke="#757575" stroke-width="1.5"/><path d="M10 7c-2 1-3 3-2 6 1 4 5 8 9 10 3 1 5 0 6-2l-3-3-2 2c-2-1-4-3-5-5l2-2-3-3z" fill="#757575"/></svg>
      +971 50 000 1234
    </div>

    <div class="side-heading" style="top:496px">EDUCATION</div>
    <div class="side-block" style="top:556px">
      <h4>University of Paris Rive Gauche – France</h4>
      <ul>
        <li>Master degree in Litigation, Arbitration, and Alternative Dispute Resolution (98/99)</li>
        <li>Master degree in commercial law (97-98)</li>
      </ul>
      <h4>Institute of Legal Studies Lutèce - France (97-98)</h4>
      <ul></ul>
      <h4>University of Orontes – Syria</h4>
      <ul><li>Law degree (92-96)</li></ul>
    </div>

    <div class="side-heading" style="top:840px">OTHERS</div>
    <div class="side-block" style="top:904px">
      <ul>
        <li>Nationalities: French - Syrian</li>
        <li>Married, 3 children</li>
        <li>Languages: Arabic, English, French.</li>
        <li>Member of the Francophone Business Circle in the Gulf and the Riverside Social Club</li>
        <li>Member in various NGO's and association working towards Women Empowerment and education of children refugee</li>
      </ul>
    </div>
  </aside>

  <main class="main-col">
    <section class="summary">
      <h2 class="section-bar">SUMMARY</h2>
      <p>A senior qualified legal professional with more than 15 years of experience in private practice and in-house focusing on the following industries: Real Estate, Retail and Services, obtained in UAE, France and Syria. Practice transactional skills (M&amp;A, real estate, commercial, corporate restructuring, strategic funding), organizational skills (policies and procedures and authority matrix covering different contexts in corporate environment), lawyering skills (preemptive legal advice, and a multi jurisdiction litigation management expertise), managerial skills (enhancing the value add of the legal department as both a service provider and a risk gatekeeper).</p>
      <p>Joined Qasr Al Noor Group in November 2011, an internationally recognized industry Leader in shopping malls, communities, retail and leisure across the Middle East, Africa and Asia, first as Legal Counsel at Qasr Al Noor Properties responsible for UAE Shopping Malls, Project management and communities, and then moved in Mai 2015 to Qasr Al Noor Retail -Marché Plus where currently I occupy the role of GM-Legal, focusing mainly on leading and managing the legal, compliance and risk management strategies across a wide geographic area of countries.</p>
      <p>Prior to moving to Dubai, I have lived in Paris France, where I have worked in various organizations including the Global Court of Arbitration, a billing software company and a consultancy practice. I graduated from University of Paris Rive Gauche with two Master Degrees.</p>
      <p>Mother of Three, I am passionate about Bon Fide work towards Women Empowerment and Refugee Children Education.</p>
    </section>

    <section class="experience">
      <h2 class="section-bar">EXPERIENCE</h2>
      <div class="role"><span class="dates">April 2017 - Present</span><span class="title">General Manager Legal at Qasr Al Noor-Marché Plus (“QANR”)</span></div>
      <div class="role"><span class="dates">May 2015 - April 2017</span><span class="title">Senior Legal Counsel at Qasr Al Noor Retail Marché Plus</span></div>
      <div class="desc">
        <h3>Description of Position</h3>
        <p>Lead and manage the legal, compliance, functions and risk management function for QANR operations in Syria, Lebanon, Jordan, Iraq, Egypt, Georgia, Armenia and Pakistan (“Countries ”). A Legal Business Partner to drive business development agenda (organically, M&amp;A, digital/ecommerce), and contribute to functional strategies.</p>
      </div>
    </section>
  </main>

  <div class="cv-footer"></div>
</section>

<!-- page 2 -->
<section class="sheet sheet-2">
  <div class="two-col">
    <div>
      <h5>Key Responsibilities</h5>
      <h6>Legal Division Leadership</h6>
      <ul>
        <li>Set the legal strategy and plan in line with group goals.</li>
        <li>Lead the legal team across the Countries.</li>
        <li>Coordinate with management and heads of business units.</li>
      </ul>
      <h6>Digital</h6>
      <ul><li>Advise on legal aspects of digital and e-commerce projects.</li></ul>
      <h6>Corporate Governance &amp; Compliance</h6>
      <ul>
        <li>Create and ensure protection of intellectual property.</li>
        <li>Apply group corporate policies.</li>
        <li>Develop and maintain legal processes and templates.</li>
      </ul>
      <h6>Others</h6>
      <ul>
        <li>Review and negotiate contracts with finance and procurement.</li>
        <li>Prepare board papers and updates to senior management.</li>
      </ul>
    </div>
    <div>
      <h6>M&amp;A</h6>
      <p>Contribute to structuring and legal review of acquisitions and disposals.</p>
      <h6>Business Development Partnership</h6>
      <p>Lead and implement legal aspects of new country partnerships, franchise and joint venture agreements.</p>
      <h6>Risk Management</h6>
      <p>Lead the implementation of control measures and risk reporting across operations.</p>
    </div>
  </div>
  <div class="entry">
    <div class="when">Nov 2011 - May 2015</div>
    <div class="what">
      <h5>Legal Counsel at Qasr Al Noor Properties LLC (“QANP”) - Dubai</h5>
      <h5>Description of Position:</h5>
      <p>Lead and manage the legal function related to the group shopping malls, communities and project management.</p>
      <h5>Key responsibilities:</h5>
      <ul>
        <li>Prepared and reviewed all contracts related to mall operations and development.</li>
        <li>Provided legal advice and opinions on matters related to the business.</li>
      </ul>
    </div>
  </div>
</section>

<!-- page 3 -->
<section class="sheet sheet-3">
  <div class="entry">
    <div class="when">Nov 2011 - May 2015</div>
    <div class="what">
      <h5>Key responsibilities:</h5>
      <ul>
        <li>Handled pre-litigation cases, sending notices and preparing settlement agreements.</li>
        <li>Negotiated with outside parties and internal clients on commercial deals.</li>
        <li>Prepared various agreements related to business development across the region.</li>
        <li>Participated in drafting leasing and management contracts for new malls.</li>
        <li>Provided internal training on standard templates and legal documents.</li>
        <li>Coached and supervised the work of the paralegal team.</li>
      </ul>
    </div>
  </div>
  <div class="entry" style="margin-top:150px">
    <div class="when">Feb 2009 - Nov 2011</div>
    <div class="what">
      <h5>Rami Noor Lawyer Services, Dubai: Legal consultant</h5>
      <h5>Description of Position:</h5>
      <p>Legal practice focusing on real estate litigation and alternative dispute resolution.</p>
      <h5>Key responsibilities:</h5>
      <ul>
        <li>Acted in real estate litigation representing developers.</li>
        <li>Acted in mediation and conciliation of real estate disputes.</li>
      </ul>
    </div>
  </div>
</section>

<!-- page 4 -->
<section class="sheet sheet-4">
  <div class="entry">
    <div class="when">Nov 2005 - Feb 2009</div>
    <div class="what">
      <h5>Key responsibilities:</h5>
      <ul>
        <li>Advised clients on setting up business in the U.A.E.</li>
        <li>Drafted and reviewed commercial, corporate and real estate agreements.</li>
        <li>Registered trademarks and advised on intellectual property matters.</li>
        <li>Negotiated and drafted agency and distribution contracts.</li>
      </ul>
    </div>
  </div>
  <div class="entry">
    <div class="when">Jan 2004 - Jun 2005</div>
    <div class="what">
      <h5>Veloris Consulting Paris - France</h5>
      <h5>Responsible of legal and administrative affairs</h5>
      <ul>
        <li>Prepared and reviewed the contracts of the company.</li>
        <li>Ensured compliance with French laws and regulation.</li>
      </ul>
    </div>
  </div>
  <div class="entry">
    <div class="when">Jun 1999 - Jun 2002</div>
    <div class="what">
      <h5>Logivia SA - In house legal counsel of a software solution company - Paris</h5>
      <ul>
        <li>Handled the legal aspects of the acquisition by a German fund.</li>
        <li>Prepared and reviewed the contracts and legal documents.</li>
      </ul>
    </div>
  </div>
  <div class="entry">
    <div class="when">Mar - Nov 2000</div>
    <div class="what">
      <h5>Global Court of Arbitration Paris - France: Assistant Counsel in the Secretariat</h5>
      <ul>
        <li>Counselled and drafted correspondence concerning all aspects of arbitration cases.</li>
        <li>Summarized procedural draft awards before scrutiny.</li>
      </ul>
    </div>
  </div>
  <div class="entry">
    <div class="when">Feb - Apr 1999</div>
    <div class="what">
      <h5>Morel Avocats, Paris - France: Trainee in the law firm</h5>
      <ul>
        <li>Prepared files in arbitration cases.</li>
        <li>Researched work in business law.</li>
      </ul>
    </div>
  </div>
</section>

<!-- page 5 -->
<section class="sheet sheet-5">
  <div class="entry">
    <div class="when">May - September 1997</div>
    <div class="what">
      <h5>Samir Nasr Office - Syria: Trainee in the law firm</h5>
      <ul>
        <li>Activities in the field of civil, commercial and criminal law.</li>
        <li>Drafted commercial contracts.</li>
      </ul>
    </div>
  </div>
  <div class="entry">
    <div class="when">June - September 1995, 1996</div>
    <div class="what">
      <h5>Karim Aziz Office, Syria: Trainee in the law firm of a professor specialist in commercial law.</h5>
      <ul>
        <li>Prepared files in the field of international commercial arbitration.</li>
      </ul>
    </div>
  </div>
</section>

</body>
</html>
```